Jewelry Business card for general purpose. Elegant and simple

We are a jewelry group with 6 stores in Mexico and 30 years in business.

We need a BC that at leats includes the name, mail, phone number and physical location (street, municipality, and county; example "Paseo Olmeda 2140", "Avenida Sotillo", "Monterrey").
Optional: we are trying to reposition the brand with the association of life-events or moments and family. Such as: birth, marriage, graduation, birthdays. Christmast, mothers day and fathers day.

We are looking for something elegant but simple

Jewelry name: "Lunetti". Email: "lunettibrillo@correo-ejemplo.mx". Phone num "4172-3095".

Target Market(s)

General business card: from suppliers to clients. One segment outstand: couples gettineg married

Industry/Entity Type

Jewelry Store

Contact Information for Business Card

Loking for something simple but elegant.

Font styles to use
Decorative
Script

Requirements
Must have
• Must have name, address, and mail.
Nice to have
• It could have jewelry pictures/design. Maybe quotes. Or general words as background . currently we have a very simple card with one ring would like to see something different.
Should not have
• Include real people.

```html
<!DOCTYPE html>
<html lang="es">
<head>
<meta charset="utf-8">
<title>Lunetti – Tarjeta de presentación</title>
<link rel="stylesheet" href="https://fonts.googleapis.com/css2?family=Great+Vibes&family=Cormorant+Garamond:wght@500;600&display=swap">
<style>
  :root {
    --backdrop: #ecebe8;
    --card: #ffffff;
    --gold: #e9b666;
    --gold-deep: #b27a2a;
    --bronze: #8d5a1c;
    --ornament: #f3e3c9;
    --ink-light: #fffaf0;
  }
  html, body {
    margin: 0;
    width: 1200px;
    height: 1021px;
    overflow: hidden;
    background: var(--backdrop);
  }
  .canvas {
    position: relative;
    width: 1200px;
    height: 1021px;
  }
  .card {
    position: absolute;
    left: 100px;
    top: 225px;
    width: 1000px;
    height: 570px;
    background: var(--card);
    box-shadow: 0 10px 30px rgba(0,0,0,0.15);
    overflow: hidden;
  }
  .card-art {
    position: absolute;
    inset: 0;
  }
  .brand {
    position: absolute;
    left: 130px;
    top: 110px;
    width: 430px;
    text-align: center;
  }
  .brand-mark {
    display: block;
    width: 44px;
    height: 44px;
    margin: 0 auto 14px;
    border: 3px solid var(--gold-deep);
    border-radius: 50%;
  }
  .brand-name {
    margin: 0;
    font-family: "Great Vibes", cursive;
    font-weight: 400;
    font-size: 140px;
    line-height: 1.25;
    color: var(--gold-deep);
  }
  .brand-tagline {
    margin: 12px 0 0;
    font-family: "Cormorant Garamond", serif;
    font-weight: 500;
    font-size: 22px;
    letter-spacing: 1px;
    color: var(--bronze);
  }
  .contact {
    position: absolute;
    left: 890px;
    top: 40px;
    width: 480px;
    transform-origin: 0 0;
    transform: rotate(90deg);
    font-family: "Cormorant Garamond", serif;
    font-weight: 600;
    font-size: 22px;
    line-height: 1.55;
    color: var(--ink-light);
    list-style: none;
    margin: 0;
    padding: 0;
  }
  .contact li {
    display: flex;
    align-items: center;
    gap: 12px;
  }
  .contact svg {
    width: 20px;
    height: 20px;
    flex: none;
  }
  .contact .indent { padding-left: 32px; }
</style>
</head>
<body>
<main class="canvas">
  <section class="card" aria-label="Tarjeta de presentación de Lunetti">
    <svg class="card-art" viewBox="0 0 1000 570" width="1000" height="570">
      <defs>
        <linearGradient id="ornament-fade" x1="0" y1="0" x2="0" y2="1">
          <stop offset="0" stop-color="#f3e3c9" stop-opacity="0.9"/>
          <stop offset="1" stop-color="#f3e3c9" stop-opacity="0"/>
        </linearGradient>
        <linearGradient id="ornament-rise" x1="0" y1="1" x2="0" y2="0">
          <stop offset="0" stop-color="#f3e3c9" stop-opacity="0.95"/>
          <stop offset="1" stop-color="#f3e3c9" stop-opacity="0"/>
        </linearGradient>
      </defs>
      <rect class="ornament-top" x="0" y="0" width="760" height="100" fill="url(#ornament-fade)" role="img" aria-label="Filigrana ornamental en tono crema"/>
      <rect class="ornament-bottom" x="0" y="400" width="660" height="170" fill="url(#ornament-rise)" role="img" aria-label="Filigrana ornamental en tono crema"/>
      <path class="band" d="M720 0 C640 120 720 260 660 360 C615 440 560 500 560 570 L1000 570 L1000 0 Z" fill="var(--gold)"/>
      <path class="band-edge" d="M700 0 C620 120 700 260 640 360 C595 440 540 500 540 570" fill="none" stroke="var(--gold-deep)" stroke-width="6"/>
      <path class="band-line" d="M740 0 C660 120 740 260 680 360 C635 440 580 500 580 570" fill="none" stroke="#ffffff" stroke-width="2" opacity="0.8"/>
    </svg>

    <div class="brand">
      <span class="brand-mark" aria-hidden="true"></span>
      <h1 class="brand-name">Lunetti</h1>
      <p class="brand-tagline">for all your life events</p>
    </div>

    <ul class="contact">
      <li>
        <svg viewBox="0 0 20 20" aria-hidden="true"><path d="M5 2 L8 2 L9 6 L7 8 C8 10 10 12 12 13 L14 11 L18 12 L18 15 C18 17 16 18 14 18 C8 17 3 12 2 6 C2 4 3 2 5 2 Z" fill="#fffaf0"/></svg>
        4172-3095
      </li>
      <li>
        <svg viewBox="0 0 20 20" aria-hidden="true"><rect x="2" y="4" width="16" height="12" rx="1" fill="none" stroke="#fffaf0" stroke-width="2"/><path d="M2 5 L10 11 L18 5" fill="none" stroke="#fffaf0" stroke-width="2"/></svg>
        lunettibrillo@correo-ejemplo.mx
      </li>
      <li>
        <svg viewBox="0 0 20 20" aria-hidden="true"><path d="M10 1 C6 1 3 4 3 8 C3 13 10 19 10 19 C10 19 17 13 17 8 C17 4 14 1 10 1 Z" fill="#fffaf0"/><circle cx="10" cy="8" r="3" fill="var(--gold)"/></svg>
        Paseo Olmeda 2140, Avenida Sotillo
      </li>
      <li class="indent">Monterrey</li>
    </ul>
  </section>
</main>
</body>
</html>
```